Postgraduate uni student association - promotion of all the great things we do for students

Poster Design – size AO
We need a poster to promote the services (KRPA) we offer to on campus & online postgraduate university students. The poster needs to highlight our key services of engagement, skill development and support.

KRPA - Kestrel Ridge Postgraduate Association is a University student association specifically for Postgraduate students (PhD, Masters, Graduate Diploma and Graduate Certificates). The Association is run independently from the University and funded by student fees. The management structure is a voluntary committee and positions are filled by PG students. Two staff assist in the delivery of the services listed below.
The feeling of the poster – bright, colourful & fun but professional (for higher degree students aged mid 20’s - 75+) speak to university students but look different to the University’s collateral ( (www.kru.edu.au). (poster could have infographic feel….)

The Design is for an AO Poster – to be printed, posters will be positioned around campus. The poster is to promote the services the association provides to all on campus & online students. The services are listed below:
KRPA - Kestrel Ridge Postgraduate Association ( Logo)
Supporting students to succeed
Engage
• Social networking – dinners, lunches, events
• Conferences
• Seminars
• FB/website
Support
• Helpline
• Financial
• Advocacy
• Mentoring
Skills Development
• Summit Workshop Series
• Resources
• Presentation
• Management
By students for students
FB www.krpa.net.au QR
Harbour Point | Ferndale | Kestrel Bay

```html
<!DOCTYPE html>
<html lang="en">
<head>
<meta charset="utf-8">
<title>KRPA – Supporting students to succeed</title>
<link rel="stylesheet" href="https://fonts.googleapis.com/css2?family=Arimo:wght@400;700&family=Tinos:ital@1&display=swap">
<style>
  :root {
    --brand-blue: #21409a;
    --brand-blue-deep: #1a3584;
    --ink: #1b2747;
    --paper: #f5f4f2;
    --paper-edge: #e2e1de;
    --teal: #3cbcb4;
    --closing-blue: #2a56b8;
    --note-yellow: #f3e03c;
    --note-lime: #c9da4a;
    --note-orange: #f1a53a;
    --white: #ffffff;
  }
  * { box-sizing: border-box; margin: 0; padding: 0; }
  html, body { width: 847px; height: 1200px; overflow: hidden; }
  body { font-family: "Arimo", Arial, sans-serif; background: var(--white); }

  .poster {
    position: relative;
    width: 847px; height: 1200px;
    background: radial-gradient(ellipse at 50% 55%, var(--paper) 55%, var(--paper-edge) 100%);
    overflow: hidden;
  }

  .masthead {
    position: absolute; left: 0; top: 0;
    width: 847px; height: 300px;
    background: linear-gradient(180deg, var(--brand-blue) 0%, var(--brand-blue-deep) 100%);
    color: var(--white);
    text-align: center;
  }
  .masthead__name {
    padding-top: 30px;
    font-weight: 400;
    font-size: 104px;
    line-height: 1;
    letter-spacing: 10px;
  }
  .masthead__full {
    margin-top: 26px;
    font-size: 30px;
    line-height: 1;
  }
  .masthead__tagline {
    margin-top: 12px;
    font-family: "Tinos", "Times New Roman", serif;
    font-style: italic;
    font-size: 44px;
    line-height: 1;
  }

  .section-title {
    position: absolute;
    font-weight: 700;
    color: var(--ink);
    line-height: 1;
    text-shadow: 1px 2px 2px rgba(0,0,0,0.2);
  }
  .section-title--engage { left: 42px; top: 352px; font-size: 50px; }
  .section-title--support { left: 578px; top: 624px; font-size: 50px; }
  .section-title--skills { left: 42px; top: 906px; font-size: 50px; }

  .note {
    position: absolute;
    display: flex; align-items: center; justify-content: center;
    font-size: 21px;
    line-height: 1.1;
    color: var(--ink);
    text-align: center;
    white-space: nowrap;
    box-shadow: 2px 3px 4px rgba(0,0,0,0.25);
  }
  .note--yellow { background: var(--note-yellow); }
  .note--lime { background: var(--note-lime); }
  .note--orange { background: var(--note-orange); }

  .circle-photo {
    position: absolute;
    left: 114px; top: 468px;
    width: 380px; height: 380px;
    border-radius: 50%;
    background: radial-gradient(circle at 50% 50%, #d9b08c 0%, #b8876a 40%, #9fb7d8 75%, #dfe6ef 100%);
  }

  .arrows { position: absolute; left: 0; top: 0; }

  .closing {
    position: absolute; left: 0; width: 847px; top: 1084px;
    text-align: center;
    font-weight: 700;
    font-size: 40px;
    color: var(--closing-blue);
  }
  .contact {
    position: absolute; left: 0; width: 847px; top: 1140px;
    text-align: center;
    font-weight: 700;
    font-size: 17px;
    color: var(--ink);
  }
</style>
</head>
<body>
<main class="poster">
  <header class="masthead">
    <div class="masthead__name">KRPA</div>
    <div class="masthead__full">kestrel ridge postgraduate association</div>
    <div class="masthead__tagline">Supporting students to succeed</div>
  </header>

  <svg class="arrows" width="847" height="1200" viewBox="0 0 847 1200" aria-hidden="true">
    <defs>
      <marker id="arrowhead" markerWidth="5" markerHeight="5" refX="2.5" refY="2.5" orient="auto">
        <path d="M0,0 L5,2.5 L0,5 Z" fill="#3cbcb4"/>
      </marker>
    </defs>
    <g fill="none" stroke="#3cbcb4" stroke-width="8" stroke-linecap="round">
      <path d="M150,880 C70,780 60,580 150,470" marker-end="url(#arrowhead)"/>
      <path d="M180,430 C320,370 470,420 530,560" marker-end="url(#arrowhead)"/>
      <path d="M540,800 C480,880 300,900 170,880" marker-end="url(#arrowhead)"/>
    </g>
  </svg>

  <h2 class="section-title section-title--engage">ENGAGE</h2>
  <div class="note note--orange" style="left:262px;top:326px;width:272px;height:74px;transform:rotate(-1deg);">Social networking -<br>dinners, lunches, events</div>
  <div class="note note--lime" style="left:262px;top:396px;width:194px;height:42px;transform:rotate(1deg);">Conferences</div>
  <div class="note note--yellow" style="left:470px;top:394px;width:116px;height:42px;transform:rotate(-1.5deg);">Seminars</div>
  <div class="note note--lime" style="left:612px;top:394px;width:154px;height:42px;transform:rotate(1deg);">FB/website</div>

  <div class="circle-photo" role="img" aria-label="Photo of many hands clasped together in a ring, seen from above"></div>

  <h2 class="section-title section-title--support">SUPPORT</h2>
  <div class="note note--orange" style="left:630px;top:700px;width:132px;height:40px;transform:rotate(-1deg);">Helpline</div>
  <div class="note note--yellow" style="left:556px;top:756px;width:130px;height:42px;transform:rotate(1deg);">Financial</div>
  <div class="note note--lime" style="left:628px;top:800px;width:140px;height:40px;transform:rotate(-1deg);">Advocacy</div>
  <div class="note note--yellow" style="left:560px;top:854px;width:156px;height:42px;transform:rotate(1.5deg);">Mentoring</div>

  <h2 class="section-title section-title--skills">SKILLS DEVELOPMENT</h2>
  <div class="note note--lime" style="left:282px;top:968px;width:350px;height:42px;transform:rotate(-0.5deg);">Summit Workshop Series</div>
  <div class="note note--yellow" style="left:93px;top:1006px;width:170px;height:42px;transform:rotate(1deg);">Resources</div>
  <div class="note note--lime" style="left:333px;top:1022px;width:203px;height:44px;transform:rotate(-1deg);">Presentation</div>
  <div class="note note--orange" style="left:565px;top:1025px;width:175px;height:44px;transform:rotate(1deg);">Management</div>

  <p class="closing">By students for students</p>
  <p class="contact">FB www.krpa.net.au QR &nbsp;|&nbsp; Harbour Point &nbsp;|&nbsp; Ferndale &nbsp;|&nbsp; Kestrel Bay</p>
</main>
</body>
</html>
```